Visitenkarten-Design für Immobilienunternehmen
Zielgruppe
Wir sind ein Immobilienunternehmen mit 2 Büros - alle Zielgruppen, jung und alt, arm und reich, Käufer und Verkäufer, privat und gewerblich suchen ein neues hochwertiges Design für die Visitenkarte
Aufgabenstellung
seriös, nicht angestaubt, Firmenfarben (rot,blau, weiß, siehe Bilder)
2-seitg bedruckt (allgemein auf der einen Seite, personenvorstellung mit bild auf der anderen seite)
Ein Visitenkartendesign für 2 Personen

```html
<!DOCTYPE html>
<html lang="de">
<head>
<meta charset="utf-8">
<title>Visitenkarte – Jens Wallner</title>
<link href="https://fonts.googleapis.com/css2?family=Raleway:wght@300;400;900&display=swap" rel="stylesheet">
<style>
  :root {
    --brand-blue: #0a2b8f;
    --brand-red: #ea150c;
    --paper: #ffffff;
    --portrait-dark: #4a5a4a;
    --portrait-mid: #8a96a8;
    --portrait-light: #c9cfc2;
  }
  html, body {
    margin: 0;
    padding: 0;
    width: 1200px;
    height: 776px;
    overflow: hidden;
    background: var(--paper);
  }
  .card {
    position: relative;
    width: 1200px;
    height: 776px;
    box-sizing: border-box;
    padding: 17px;
    background: linear-gradient(90deg, var(--brand-blue) 0%, var(--brand-red) 100%);
    font-family: "Raleway", sans-serif;
    color: var(--brand-blue);
  }
  .card__inner {
    position: relative;
    width: 100%;
    height: 100%;
    background: var(--paper);
  }
  .portrait {
    position: absolute;
    left: 65px;
    top: 65px;
    width: 392px;
    height: 392px;
    box-sizing: border-box;
    border-radius: 50%;
    border: 11px solid var(--brand-blue);
    background: radial-gradient(circle at 50% 40%, var(--portrait-light) 0%, var(--portrait-mid) 55%, var(--portrait-dark) 100%);
  }
  .person {
    position: absolute;
    left: 521px;
    top: 62px;
  }
  .person__name {
    margin: 0;
    font-weight: 900;
    font-size: 68px;
    line-height: 1;
    letter-spacing: -0.5px;
  }
  .person__role {
    margin: 22px 0 0;
    font-weight: 400;
    font-size: 45px;
    line-height: 54px;
  }
  .person__phone {
    margin: 86px 0 0;
    font-weight: 900;
    font-size: 64px;
    line-height: 1;
    color: var(--brand-red);
    font-variant-numeric: oldstyle-nums;
  }
  .invitation {
    position: absolute;
    left: 54px;
    top: 552px;
    margin: 0;
    width: 1000px;
    font-weight: 400;
    font-size: 46px;
    line-height: 54px;
  }
</style>
</head>
<body>
  <div class="card">
    <div class="card__inner">
      <div class="portrait" role="img" aria-label="Porträtfoto von Jens Wallner im Anzug"></div>
      <div class="person">
        <h1 class="person__name">Jens Wallner</h1>
        <p class="person__role">Geschäftsführer<br>Veromilk/Orbis Gutachter<br>für Immobilienbewertung</p>
        <p class="person__phone">0172/5518640</p>
      </div>
      <p class="invitation">Kennen Sie jemanden, der ein Haus oder eine Wohnung kaufen oder verkaufen möchte? Bitte rufen Sie mich an. Ich freue mich!</p>
    </div>
  </div>
</body>
</html>
```